The Pixel Tap Business card.

A Simple card with our Logo and contact information. To give to investors and other professionals.

We are a nerd themed bar.
our target market is young professionals age 21+ but the real purpose of this business card is to present to potential investors and other professionals with our contact information. as we are still looking for funding before we start up.

I am partial to green and my partner likes red we are open to iteration.

Target Market(s)

Investors

Industry/Entity Type

Business

Contact Information for Business Card

Martin Hale (225) 730-6192 kent.h4711@mailnest.test Glen Porter (225) 968-5037 glenp318@mailnest.test

Font styles to use
Serif

Requirements
Nice to have
• Keep it simple but not boring.
• Use the Logos but feel free to edit them to match theme/colors.
• Keep the back clean and use one of the Logos.

```html
<!DOCTYPE html>
<html lang="en">
<head>
<meta charset="utf-8">
<title>The Pixel Tap – Business Cards</title>
<link rel="stylesheet" href="https://fonts.googleapis.com/css2?family=Cinzel:wght@400&family=Source+Sans+3:ital,wght@0,400;0,700;1,400&display=swap">
<style>
  :root {
    --backdrop: #cccccc;
    --card: #f5f5f5;
    --ink: #1e1e1e;
    --green: #07904a;
    --red: #dc2a22;
    --logo-ink: #111111;
  }
  * { margin: 0; padding: 0; box-sizing: border-box; }
  html, body {
    width: 1200px;
    height: 736px;
    overflow: hidden;
    background: var(--backdrop);
  }
  .canvas {
    position: relative;
    width: 1200px;
    height: 736px;
  }
  .card {
    position: absolute;
    width: 433px;
    height: 261px;
    background: var(--card);
    overflow: hidden;
  }
  .card--back { left: 372px; top: 89px; display: flex; align-items: center; justify-content: center; }
  .card--martin { left: 150px; top: 384px; --accent: var(--green); }
  .card--glen { left: 617px; top: 384px; --accent: var(--red); }

  .brand {
    display: flex;
    align-items: center;
    gap: 10px;
    font-family: "Source Sans 3", sans-serif;
    font-weight: 700;
    font-size: 32px;
    letter-spacing: 0.5px;
    color: var(--logo-ink);
    text-transform: uppercase;
  }
  .brand__dot {
    width: 16px;
    height: 16px;
    border-radius: 50%;
    background: var(--red);
  }

  .name-frame {
    position: absolute;
    left: 128px;
    top: 73px;
    width: 177px;
    height: 41px;
    border: 1px solid var(--accent);
    display: flex;
    align-items: center;
    justify-content: center;
  }
  .name {
    font-family: "Cinzel", serif;
    font-weight: 400;
    font-size: 21px;
    color: var(--ink);
    letter-spacing: 0.3px;
    white-space: nowrap;
  }
  .role {
    position: absolute;
    left: 50%;
    bottom: 0;
    transform: translate(-50%, 50%);
    padding: 0 10px;
    background: var(--card);
    font-family: "Source Sans 3", sans-serif;
    font-style: italic;
    font-size: 10.5px;
    color: var(--accent);
    white-space: nowrap;
  }
  .contact {
    position: absolute;
    left: 0;
    right: 0;
    top: 141px;
    text-align: center;
    font-family: "Source Sans 3", sans-serif;
    font-size: 12px;
    line-height: 19.5px;
    color: var(--ink);
  }
  .accent-band {
    position: absolute;
    left: 0;
    right: 0;
    top: 249px;
    height: 13px;
    background: var(--accent);
  }
</style>
</head>
<body>
<main class="canvas">
  <section class="card card--back">
    <div class="brand">
      <span class="brand__dot"></span>
      <span class="brand__name">The Pixel Tap</span>
    </div>
  </section>

  <section class="card card--martin">
    <div class="name-frame">
      <h1 class="name">Martin Hale</h1>
      <span class="role">Director</span>
    </div>
    <p class="contact">(225) 730-6192<br>kent.h4711@mailnest.test</p>
    <div class="accent-band"></div>
  </section>

  <section class="card card--glen">
    <div class="name-frame">
      <h1 class="name">Glen Porter</h1>
      <span class="role">Director</span>
    </div>
    <p class="contact">(225) 968-5037<br>glenp318@mailnest.test</p>
    <div class="accent-band"></div>
  </section>
</main>
</body>
</html>
```